We need a home page that represents us as the best Veterinary Hospital in the State

We need webdesign for a Vet Hospital in Rio de Janeiro, Brazil.
We think the current design is very childish. We want something that looks more like a hospital and not a clinic.
We put a map to guide the content of the sections and also an example of a layout that we don't like but that may serve as a reference as a wireframe.

Target Market(s)

pet owners

Industry/Entity Type

Pet Care

Number of Pages Required

1 page

Requirements
Must have
• Here is a map of the sections and texts we think for home: https://qv.zx/4937018256?t=HpLrTnsKwe
Nice to have
• some sites we like:
https://www.valtoramed.br/Pages/Home.aspx
https://www.mediquiro.com/
Should not have
• This is a design that we started working on and the content is correct. But the layout is poor in detail, bad colors, CTA's without prominence.

https://orlenpixworks.plankview.app/console/share/KT7N2W8RXP/731905246

```html
<!DOCTYPE html>
<html lang="pt-BR">
<head>
<meta charset="utf-8">
<title>Vitalis Pet — Hospital Veterinário 24h</title>
<link href="https://fonts.googleapis.com/css2?family=Kumbh+Sans:wght@400;500;600;700;800&display=swap" rel="stylesheet">
<style>
:root{
  --blue:#0d6bb8;
  --blue-dark:#0a5ea3;
  --red:#cf0a24;
  --sky:#80b5db;
  --navy:#26364a;
  --ink:#1d1d1f;
  --grey-card:#efefef;
  --text:#3a3a3a;
  --white:#fff;
  --black:#000;
}
*{margin:0;padding:0;box-sizing:border-box}
html,body{width:1200px;height:3578px;overflow:hidden;background:var(--white)}
body{font-family:"Kumbh Sans",sans-serif;color:var(--ink);position:relative}
.abs{position:absolute}
a{color:inherit;text-decoration:none}
.btn{position:absolute;background:var(--red);color:var(--white);font-weight:700;font-size:12px;letter-spacing:.3px;display:flex;align-items:center;justify-content:center;gap:9px}
.btn svg{width:7px;height:10px}

/* hero */
.hero{left:0;top:0;width:1200px;height:679px;overflow:hidden}
.hero-photo{position:absolute;inset:0;background:linear-gradient(100deg,#3f6f9f 0%,#6f96bd 30%,#a7bcd0 50%,#b89c83 68%,#c8a3b9 82%,#8ea8c6 100%)}
.topbar{left:0;top:0;width:1200px;height:52px;color:var(--white);font-size:13px}
.topbar .mail{left:60px;top:18px;display:flex;gap:9px;align-items:center}
.topbar .call{right:56px;top:18px;display:flex;gap:8px;align-items:center}
.nav{left:34px;top:55px;width:1130px;height:67px;background:var(--white);box-shadow:0 2px 8px rgba(0,0,0,.08)}
.logo{position:absolute;display:flex;align-items:center;gap:8px;font-weight:800;color:var(--blue)}
.logo i{display:block;width:14px;height:14px;background:var(--red)}
.nav .logo{left:58px;top:20px;font-size:24px}
.menu{position:absolute;left:322px;top:27px;display:flex;gap:24px;font-size:12px;font-weight:500;color:#222}
.menu .on{border-bottom:2px solid var(--red);padding-bottom:4px}
.nav .btn{left:990px;top:20px;width:110px;height:28px;font-size:11.5px;border-radius:2px}
.hero h1{left:88px;top:262px;color:var(--white);font-size:51px;font-weight:800;line-height:1.05;letter-spacing:-.5px}
.hero .rule{left:88px;top:392px;width:200px;height:4px;background:var(--white)}
.hero p{left:88px;top:404px;width:420px;color:var(--white);font-size:20px;line-height:1.22;font-weight:500}
.hero .btn{left:88px;top:498px;width:114px;height:31px}

.services{left:111px;top:618px;width:980px;height:124px;background:var(--blue);display:flex;color:var(--white);box-shadow:0 6px 14px rgba(0,0,0,.15)}
.svc{flex:1;display:flex;flex-direction:column;align-items:center;justify-content:flex-end;padding-bottom:20px;gap:14px;font-size:14px;font-weight:600;position:relative}
.svc+ .svc::before{content:"";position:absolute;left:0;top:22px;height:72px;width:1px;background:rgba(255,255,255,.6)}
.svc svg{width:44px;height:44px;fill:none;stroke:var(--white);stroke-width:1.8;stroke-linecap:round;stroke-linejoin:round}

/* section heads */
.head{left:0;width:1200px;text-align:center}
.head h2{font-size:32px;font-weight:700;color:var(--ink)}
.bars{display:flex;justify-content:center;gap:10px;margin-top:14px}
.bars span{height:4px;background:var(--ink);width:180px}
.bars span+span{width:36px}

/* units */
.unit{top:933px;width:290px;height:367px;background:var(--grey-card);box-shadow:0 2px 6px rgba(0,0,0,.12)}
.unit .photo{height:162px}
.unit h3{position:absolute;left:26px;top:184px;font-size:17px;font-weight:600}
.unit .u-rule{position:absolute;left:26px;top:213px;width:44px;height:2px;background:#555}
.unit p{position:absolute;left:26px;top:229px;width:240px;font-size:13px;line-height:1.6;color:var(--text)}
.unit small{position:absolute;left:26px;top:280px;font-size:11px;color:var(--text)}
.unit .map{position:absolute;right:24px;top:328px;font-size:11px;display:flex;gap:16px;align-items:center}

/* split */
.split-photo{left:0;top:1409px;width:612px;height:441px;background:linear-gradient(135deg,#5e6468 0%,#9ea6ab 35%,#dfe3e5 55%,#3aa0c0 75%,#1a7f9f 100%)}
.play{left:269px;top:1518px;width:56px;height:56px;border-radius:50%;background:var(--white);display:flex;align-items:center;justify-content:center}
.split-copy{left:612px;top:1409px;width:588px;height:441px;background:var(--sky);color:var(--white)}
.split-copy h2{position:absolute;left:49px;top:107px;width:500px;font-size:32px;line-height:1.33;font-weight:700;letter-spacing:.3px}
.split-copy p{position:absolute;left:49px;top:239px;font-size:23px;font-weight:600}
.split-copy .btn{left:49px;top:288px;width:114px;height:31px}

/* cta strip */
.cta h2{left:183px;top:1897px;font-size:32px;font-weight:700}
.cta p{left:183px;top:1943px;width:560px;font-size:13px;line-height:1.55;color:var(--text)}
.cta .btn{left:1059px;top:1905px;width:135px;height:38px;font-size:13px}

/* testimonials */
.testi{left:0;top:2044px;width:1200px;height:443px;background:linear-gradient(90deg,#2a3a4e,#233244 50%,#2c3e52)}
.testi .kicker{position:absolute;left:0;width:1200px;top:38px;text-align:center;color:var(--white);font-size:15px;font-weight:600}
.testi h2{position:absolute;left:0;width:1200px;top:66px;text-align:center;color:var(--white);font-size:32px;font-weight:700}
.testi .bars{position:absolute;left:0;width:1200px;top:108px}
.testi .bars span{background:var(--white);width:190px}
.testi .bars span+span{width:36px}
.avatar{position:absolute;left:230px;top:193px;width:96px;height:96px;transform:rotate(45deg);border:4px solid var(--white);outline:3px solid var(--blue);background:linear-gradient(160deg,#c8d4e0,#8a9db0)}
.quote{position:absolute;color:var(--white);font-size:46px;font-weight:800;line-height:1}
.testi blockquote{position:absolute;left:408px;top:226px;width:560px;color:var(--white);font-size:14px;line-height:1.5}
.testi cite{position:absolute;left:408px;top:326px;color:var(--white);font-style:normal;font-size:18px;font-weight:600}
.arrows{position:absolute;left:912px;top:350px;display:flex;gap:22px}
.arrows svg{width:14px;height:22px;stroke:var(--white);stroke-width:2.6;fill:none}

/* blog */
.blog .kicker{color:var(--blue);font-size:15px;font-weight:600}
.post{top:2709px;width:380px;height:389px;background:var(--grey-card)}
.post .photo{height:206px}
.post .date{position:absolute;left:22px;top:230px;font-size:11px;display:flex;gap:10px;align-items:center}
.post p{position:absolute;left:22px;top:256px;width:330px;font-size:14px;line-height:1.5;color:var(--text)}
.post .go{position:absolute;right:20px;top:345px}
.blog .btn{left:720px;top:3150px;width:115px;height:33px}

/* footer */
.footer{left:0;top:3248px;width:1200px;height:330px;background:var(--black);color:var(--white)}
.footer .logo{left:115px;top:50px;font-size:30px;color:var(--white)}
.footer .tag{position:absolute;left:115px;top:105px;width:210px;font-size:11.5px;font-weight:600;line-height:1.35}
.social{position:absolute;left:115px;top:150px;display:flex;gap:16px}
.social span{width:19px;height:19px;border-radius:50%;border:2px solid var(--white);display:block}
.col{position:absolute;top:80px;font-size:11px;line-height:1.85}
.col h4{font-size:13px;font-weight:700;letter-spacing:.4px;margin-bottom:12px}
.col .ph{display:flex;gap:10px;align-items:center;font-size:13px;line-height:2.2}
.footer .rt{position:absolute;left:0;width:1200px;top:266px;text-align:center;font-size:12px}
.footer .line{position:absolute;left:215px;width:770px;top:290px;height:1px;background:#777}
.footer .copy{position:absolute;left:0;width:1200px;top:304px;text-align:center;font-size:10px}
</style>
</head>
<body>

<header class="hero abs">
  <div class="hero-photo" role="img" aria-label="Veterinária de luvas examinando um pequeno cão de pelo longo na mesa de atendimento"></div>

  <div class="topbar abs">
    <div class="mail abs">
      <svg width="16" height="12" viewBox="0 0 16 12" fill="none" stroke="#fff" stroke-width="1.3"><rect x="1" y="1" width="14" height="10" rx="1"/><path d="M1 1l7 6 7-6"/></svg>
      Email Us: contato@vitalispet.com
    </div>
    <div class="call abs">
      <svg width="12" height="14" viewBox="0 0 12 14" fill="#fff"><path d="M2 1l3 0 1 3-2 1.5c.8 2 2 3.3 3.7 4.2L9.3 8l2.7 1v3c-5.5.5-11-5-10-11z"/></svg>
      Call Us: +55 21 3000-0100
    </div>
  </div>

  <nav class="nav abs">
    <div class="logo"><i></i>Vitalis Pet</div>
    <div class="menu">
      <span class="on">Home</span><span>Agendamentos</span><span>Vacinas</span><span>Unidades</span><span>Blog</span><span>Trabalhe</span><span>A Vitalis Pet</span><span>Area do Tutor</span>
    </div>
    <a class="btn">Get Appointment</a>
  </nav>

  <h1 class="abs">PRA CUIDAR<br>DE QUEM VOCÊ AMA!</h1>
  <div class="rule abs"></div>
  <p class="abs">Excelentes médicos e infraestrutura completa por um preço que cabe no seu bolso.</p>
  <a class="btn">VEJA MAIS <svg viewBox="0 0 7 10" fill="none" stroke="#fff" stroke-width="1.6"><path d="M1 1l4 4-4 4"/></svg></a>
</header>

<section class="services abs">
  <div class="svc">
    <svg viewBox="0 0 44 44"><circle cx="22" cy="12" r="7"/><path d="M15 9h14M8 42c0-10 6-16 14-16s14 6 14 16z"/><path d="M17 27v7a3 3 0 003 3M27 27v5"/><circle cx="27" cy="34" r="2"/></svg>
    Pronto-Socorro
  </div>
  <div class="svc">
    <svg viewBox="0 0 44 44"><path d="M12 4v10a8 8 0 0016 0V4"/><path d="M20 22v8a7 7 0 0014 0v-4"/><circle cx="34" cy="22" r="4"/></svg>
    Consultas
  </div>
  <div class="svc">
    <svg viewBox="0 0 44 44"><path d="M10 4h18l8 8v28H10z"/><path d="M28 4v8h8M16 18h14M16 24h14M16 30h14M16 35h8"/></svg>
    Resultado de Exames
  </div>
  <div class="svc">
    <svg viewBox="0 0 44 44"><circle cx="22" cy="23" r="16"/><path d="M22 13v10l7 5"/><path d="M10 8l4 3M34 8l-4 3"/></svg>
    Agendamento de Exames
  </div>
  <div class="svc">
    <svg viewBox="0 0 44 44"><path d="M30 6l8 8M34 10l-6 6M28 10L12 26l6 6 16-16"/><path d="M12 26l-6 12 12-6M16 22l3 3M20 18l3 3"/></svg>
    Vacinas
  </div>
</section>

<div class="head abs" style="top:835px">
  <h2>UNIDADES VITALIS PET</h2>
  <div class="bars"><span></span><span></span></div>
</div>

<article class="unit abs" style="left:111px">
  <div class="photo" role="img" aria-label="Veterinário examinando um cão de pelagem dourada no consultório" style="background:linear-gradient(120deg,#cfd6dc,#a7aeb4 45%,#c8904f 75%,#6a5c50)"></div>
  <h3>Taquara - RJ</h3><div class="u-rule"></div>
  <p>Pronto-Socorro, Atendimento Clínico e Especialidades</p>
  <small>Rua das Acácias, 88, Taquara</small>
  <div class="map">Veja no mapa <svg width="20" height="10" viewBox="0 0 20 10" fill="none" stroke="#0d6bb8" stroke-width="2"><path d="M0 5h17M13 1l4 4-4 4"/></svg></div>
</article>
<article class="unit abs" style="left:455px">
  <div class="photo" role="img" aria-label="Procedimento cirúrgico com instrumentos sobre campo cirúrgico azul" style="background:linear-gradient(135deg,#6a6f73,#3fa3d6 40%,#2a89c2 65%,#4e545a)"></div>
  <h3>Flamengo - RJ</h3><div class="u-rule"></div>
  <p>Pronto-Socorro, Atendimento Clínico e Especialidades</p>
  <small>Rua dos Ipês, 412, Flamengo</small>
  <div class="map">Veja no mapa <svg width="20" height="10" viewBox="0 0 20 10" fill="none" stroke="#0d6bb8" stroke-width="2"><path d="M0 5h17M13 1l4 4-4 4"/></svg></div>
</article>
<article class="unit abs" style="left:800px">
  <div class="photo" role="img" aria-label="Veterinária examinando o ouvido de um cão com otoscópio" style="background:linear-gradient(120deg,#7c8186,#c9ccce 40%,#d9b27f 70%,#8c8f93)"></div>
  <h3>Copacabana - RJ</h3><div class="u-rule"></div>
  <p>Pronto-Socorro, Atendimento Clínico e Especialidades</p>
  <small>Rua das Acácias, 88, Taquara</small>
  <div class="map">Veja no mapa <svg width="20" height="10" viewBox="0 0 20 10" fill="none" stroke="#0d6bb8" stroke-width="2"><path d="M0 5h17M13 1l4 4-4 4"/></svg></div>
</article>

<div class="split-photo abs" role="img" aria-label="Mãos com luvas azuis enfaixando a pata de um gato"></div>
<div class="play abs"><svg width="20" height="22" viewBox="0 0 20 22"><path d="M3 2l15 9-15 9z" fill="#cf0a24"/></svg></div>
<section class="split-copy abs">
  <h2>Infraestrutura completa e equipe médica disponível 24h todos os dias</h2>
  <p>Existe lugar para tudo!</p>
  <a class="btn">VEJA MAIS <svg viewBox="0 0 7 10" fill="none" stroke="#fff" stroke-width="1.6"><path d="M1 1l4 4-4 4"/></svg></a>
</section>

<section class="cta">
  <h2 class="abs">obtenha nossos serviços</h2>
  <p class="abs">Lorem ipsum dolor sit amet, consetetur sadipscing o duo dolores et ea eirmod tempor invidunt ut labore et dolore magna aliquyam erat, sed diam</p>
  <a class="btn" style="left:1059px;transform:translateX(-0%);left:1059px"></a>
</section>
<a class="btn" style="left:1059px;top:1905px;width:135px;height:38px;font-size:13px">VEJA MAIS <svg viewBox="0 0 7 10" fill="none" stroke="#fff" stroke-width="1.6"><path d="M1 1l4 4-4 4"/></svg></a>

<section class="testi abs" role="region" aria-label="Depoimentos de tutores sobre fundo com clínica veterinária">
  <div class="kicker">O que dizem alguns tutores</div>
  <h2>Pegar testemunhos do Perfil Vitalis</h2>
  <div class="bars"><span></span><span></span></div>
  <div class="avatar" role="img" aria-label="Foto de perfil do tutor"></div>
  <div class="quote" style="left:376px;top:184px">“</div>
  <blockquote>Replace this content with your own content. Content should be relevant, unique and written with the goal of providing the reader the type of information they are looking for while motivating them to</blockquote>
  <div class="quote" style="left:734px;top:290px">”</div>
  <cite>Lucas Prado</cite>
  <div class="arrows">
    <svg viewBox="0 0 14 22"><path d="M11 2L3 11l8 9"/></svg>
    <svg viewBox="0 0 14 22"><path d="M3 2l8 9-8 9"/></svg>
  </div>
</section>

<section class="blog">
  <div class="head abs" style="top:2578px">
    <div class="kicker">Você pode se interessa por</div>
    <h2 style="margin-top:10px">Último artigo do blog</h2>
    <div class="bars" style="margin-top:16px"><span></span><span></span></div>
  </div>
  <article class="post abs" style="left:182px">
    <div class="photo" role="img" aria-label="Veterinário aplicando gotas no ouvido de um cão de pelagem dourada" style="background:linear-gradient(120deg,#e8e3dc,#d59a55 45%,#b46f32 70%,#ecebe8)"></div>
    <div class="date"><svg width="12" height="12" viewBox="0 0 12 12" fill="none" stroke="#0d6bb8" stroke-width="1.2"><rect x="1" y="2" width="10" height="9"/><path d="M1 5h10M4 1v2M8 1v2"/></svg>22 MAY 2021</div>
    <p>Lorem ipsum dolor sit amet, consetetur sadipscing elitr, sed diam nonumy eirmod tempor invidunt ut labore et dolore magna</p>
    <svg class="go" width="18" height="14" viewBox="0 0 18 14" fill="none" stroke="#0d6bb8" stroke-width="2"><path d="M1 7h15M10 1l6 6-6 6"/></svg>
  </article>
  <article class="post abs" style="left:617px">
    <div class="photo" role="img" aria-label="Veterinária com estetoscópio segurando um gato cinza" style="background:linear-gradient(120deg,#1e3f72,#2c5a99 40%,#9aa1a8 70%,#d6d6d6)"></div>
    <div class="date"><svg width="12" height="12" viewBox="0 0 12 12" fill="none" stroke="#0d6bb8" stroke-width="1.2"><rect x="1" y="2" width="10" height="9"/><path d="M1 5h10M4 1v2M8 1v2"/></svg>22 MAY 2021</div>
    <p>Lorem ipsum dolor sit amet, consetetur sadipscing elitr, sed diam nonumy eirmod tempor invidunt ut labore et dolore magna</p>
    <svg class="go" width="18" height="14" viewBox="0 0 18 14" fill="none" stroke="#0d6bb8" stroke-width="2"><path d="M1 7h15M10 1l6 6-6 6"/></svg>
  </article>
  <a class="btn" style="left:542px;top:3150px;width:115px;height:33px">VEJA MAIS <svg viewBox="0 0 7 10" fill="none" stroke="#fff" stroke-width="1.6"><path d="M1 1l4 4-4 4"/></svg></a>
</section>

<footer class="footer abs">
  <div class="logo abs"><i></i>Vitalis Pet</div>
  <p class="tag">Atendimento médico veterinário de qualidade completo e acessível.</p>
  <div class="social" aria-label="Redes sociais"><span></span><span></span><span></span><span></span></div>
  <div class="col" style="left:360px"><h4>SERVIÇOS</h4>Pronto-socorro<br>Consultas<br>Exames<br>Vacinas<br>Cirurgias</div>
  <div class="col" style="left:513px"><h4>VITALIS PET</h4>Unidades<br>Blog<br>Trabalhe conosco<br>Quem somos</div>
  <div class="col" style="left:650px"><h4>TUTORES</h4>Área do tutor<br>Agendamentos<br>Resultado de exames</div>
  <div class="col" style="left:796px"><h4>AJUDA</h4>Ouvidoria<br>Fale Conosco</div>
  <div class="col" style="left:920px"><h4>CENTRAL DE ATENDIMENTO</h4>
    <div class="ph"><svg width="13" height="13" viewBox="0 0 13 13" fill="none" stroke="#fff" stroke-width="1.3"><circle cx="6.5" cy="6.5" r="5.5"/><path d="M4.5 4l1 2-1 1c.6 1 1.3 1.6 2.2 2l1-1 2 1"/></svg>+55 21 3000-0100</div>
    <div class="ph"><svg width="13" height="13" viewBox="0 0 12 14" fill="#fff"><path d="M2 1l3 0 1 3-2 1.5c.8 2 2 3.3 3.7 4.2L9.3 8l2.7 1v3c-5.5.5-11-5-10-11z"/></svg>+55 21 90000-2000</div>
  </div>
  <div class="rt">Responsável técnico; Dr. Rafael Moura - Médico Veterinário - CRMV-RJ</div>
  <div class="line"></div>
  <div class="copy">All right reserve 2021- Vitalis Pet</div>
</footer>

</body>
</html>
```